Business card required for IT Consultancy Business - Tealbrook Consulting.
Company provides the whole nine yards of services across IT Architecture, design and execution.
Basically we provide consulting services to help businesses make sure their technology is enabling their business strategy.
Design for front and back required.
We would like the front of the card to inlcude:
Name
Title
Mobile number
email address
www.tbkc.com.au
Company logos attached.
Thank you
Industry/Entity Type
Business
Contact Information for Business Card
Name
Title
Mobile number
email address
www.tbkc.com.au
Look and feel
Each slider illustrates characteristics of the customer's brand and the style your logo design should communicate.

```html
<!DOCTYPE html>
<html lang="en">
<head>
<meta charset="utf-8">
<title>Tealbrook Consulting — Business Card</title>
<link rel="stylesheet" href="https://fonts.googleapis.com/css2?family=Teko:wght@400&family=Mulish:wght@400&display=swap">
<style>
  :root {
    --orange: #f15a2b;
    --blue: #1275bb;
    --paper: #ffffff;
    --divider: #000000;
  }
  html, body {
    margin: 0;
    padding: 0;
    overflow: hidden;
    background: var(--paper);
  }
  .card-sheet {
    position: relative;
    width: 1050px;
    height: 1200px;
    overflow: hidden;
    background: var(--paper);
    color: var(--orange);
  }
  .card-face {
    position: absolute;
    left: 0;
    width: 1050px;
    height: 600px;
  }
  .card-face--front { top: 0; }
  .card-face--back { top: 600px; }
  .face-divider {
    position: absolute;
    top: 599px;
    left: 0;
    width: 1050px;
    height: 2px;
    background: var(--divider);
  }

  /* Front */
  .brand-dot {
    position: absolute;
    left: 230px;
    top: 110px;
    width: 260px;
    height: 260px;
    border-radius: 50%;
    background: var(--blue);
  }
  .brand-name {
    position: absolute;
    right: 40px;
    top: 340px;
    margin: 0;
    font-family: "Teko", sans-serif;
    font-weight: 400;
    color: var(--orange);
    text-align: right;
    line-height: 1;
  }
  .brand-name__main {
    display: block;
    font-size: 132px;
    letter-spacing: 14px;
    margin-right: -14px;
  }
  .brand-name__sub {
    display: block;
    margin-top: 26px;
    font-size: 52px;
    letter-spacing: 9px;
    margin-right: -9px;
  }
  .front-rule {
    position: absolute;
    height: 5px;
    background: var(--blue);
  }
  .front-rule--upper { left: 530px; width: 482px; top: 474px; }
  .front-rule--lower { left: 607px; width: 443px; top: 491px; }

  /* Back */
  .brand-stack {
    position: absolute;
    left: 66px;
    top: 80px;
    height: 450px;
    margin: 0;
    writing-mode: vertical-rl;
    transform: rotate(180deg);
    font-family: "Teko", sans-serif;
    font-weight: 400;
    color: var(--orange);
    text-align: center;
    line-height: 0.95;
  }
  .brand-stack__main {
    display: block;
    font-size: 92px;
    letter-spacing: 2px;
  }
  .brand-stack__sub {
    display: block;
    font-size: 58px;
    letter-spacing: 6px;
  }
  .contact-block {
    position: absolute;
    left: 340px;
    width: 636px;
    top: 70px;
    text-align: right;
  }
  .contact-name {
    margin: 0;
    font-family: "Teko", sans-serif;
    font-weight: 400;
    font-size: 72px;
    line-height: 1;
    letter-spacing: 15px;
    margin-right: -15px;
    height: 76px;
  }
  .contact-rule {
    height: 4px;
    background: var(--blue);
  }
  .contact-rule--top { margin-top: 18px; }
  .contact-details {
    margin: 38px 0 0;
    font-family: "Mulish", sans-serif;
    font-weight: 400;
    line-height: 1;
  }
  .contact-title {
    display: block;
    font-size: 35px;
    margin-bottom: 16px;
  }
  .contact-line {
    display: block;
    font-size: 30px;
    margin-bottom: 17px;
  }
  .contact-rule--bottom { margin-top: 36px; }
  .contact-web {
    margin: 22px 0 0;
    font-family: "Teko", sans-serif;
    font-weight: 400;
    font-size: 62px;
    line-height: 1;
    letter-spacing: 12px;
    margin-right: -12px;
  }
</style>
</head>
<body>
<main class="card-sheet">
  <section class="card-face card-face--front" aria-label="Card front">
    <div class="brand-dot" aria-hidden="true"></div>
    <div class="front-rule front-rule--upper" aria-hidden="true"></div>
    <div class="front-rule front-rule--lower" aria-hidden="true"></div>
    <h1 class="brand-name">
      <span class="brand-name__main">TEALBROOK</span>
      <span class="brand-name__sub">CONSULTING</span>
    </h1>
  </section>

  <div class="face-divider" aria-hidden="true"></div>

  <section class="card-face card-face--back" aria-label="Card back">
    <p class="brand-stack">
      <span class="brand-stack__main">TEALBROOK</span>
      <span class="brand-stack__sub">consulting</span>
    </p>
    <div class="contact-block">
      <h2 class="contact-name">FIRST LAST NAME</h2>
      <div class="contact-rule contact-rule--top"></div>
      <p class="contact-details">
        <span class="contact-title">VICE PRESIDENT OF OPERATIONS</span>
        <span class="contact-line">000.000.0000 :M</span>
        <span class="contact-line">000.000.0000 :F</span>
        <span class="contact-line">email.address@tbkc.com.au</span>
      </p>
      <div class="contact-rule contact-rule--bottom"></div>
      <p class="contact-web">TBKC.COM.AU</p>
    </div>
  </section>
</main>
</body>
</html>
```